Coastal Gin Label Design

We are needing a nautical/coastal themed label for our upcoming gin release.

We have saltbush, cucumber, juniper, and quandong being used in this gin.

Name of the Gin; Harbor Glow

The logo attached is the company logo, but doesn't have to be used on the front of the label, ie it can just be the name Fernwhistle somewhere on the front.
Bottle specs attached as well so you can accurately represent the bottle- this bottle is also clear.

Target Market(s)

Women 25- 45

Font styles to use
Serif
Decorative

Colors
d5edf4
86cae7
33a6d7
86cfc6
cfeae6
ffffff
f6faec
ecf7fb
fefeff

Requirements
Must have
• Ocean/Coastal vibe to the label
Nice to have
• Blues,Whites clean and crisp
Should not have
• No generic word art look to it.
A dark mood

```html
<!DOCTYPE html>
<html lang="en">
<head>
<meta charset="utf-8">
<title>Harbor Glow Gin – Front Label</title>
<link rel="stylesheet" href="https://fonts.googleapis.com/css2?family=Cormorant+Garamond:wght@500;600&family=Mrs+Saint+Delafield&display=swap">
<style>
  :root {
    --page: #fdf6f3;
    --label: #f1f0ec;
    --sand-light: #ebe4d8;
    --sand: #ddd3c3;
    --sea-pale: #d5edf4;
    --sea-light: #aed7ec;
    --sea: #86cae7;
    --sea-deep: #5fb3dc;
    --ink: #1f2a52;
    --gold: #a88a52;
    --fine: #6f7580;
  }
  * { margin: 0; padding: 0; box-sizing: border-box; }
  html, body {
    width: 849px;
    height: 1200px;
    overflow: hidden;
    background: var(--page);
  }
  .canvas {
    position: relative;
    width: 849px;
    height: 1200px;
    background: var(--page);
  }
  .label {
    position: absolute;
    left: 135px;
    top: 300px;
    width: 580px;
    height: 600px;
    background: var(--label);
    overflow: hidden;
    box-shadow: 0 2px 10px rgba(60, 50, 40, 0.06);
  }
  .sand-wash {
    position: absolute;
    left: 0;
    top: 170px;
    width: 100%;
    height: 290px;
    background: linear-gradient(180deg,
      rgba(235, 228, 216, 0) 0%,
      var(--sand-light) 18%,
      var(--sand) 55%,
      var(--sand-light) 85%,
      rgba(235, 228, 216, 0) 100%);
  }
  .sea-wash {
    position: absolute;
    left: 0;
    top: 410px;
    width: 100%;
    height: 120px;
    background: linear-gradient(180deg,
      rgba(213, 237, 244, 0.4) 0%,
      var(--sea-light) 25%,
      var(--sea) 55%,
      var(--sea-light) 80%,
      rgba(213, 237, 244, 0.3) 100%);
  }
  .brand {
    position: absolute;
    top: 78px;
    width: 100%;
    text-align: center;
    font-family: "Cormorant Garamond", serif;
    font-weight: 600;
    font-size: 20px;
    letter-spacing: 3px;
    text-transform: uppercase;
    color: var(--gold);
  }
  .gin-name {
    position: absolute;
    left: 0;
    top: 185px;
    width: 100%;
    font-family: "Mrs Saint Delafield", cursive;
    font-weight: 400;
    color: var(--ink);
    line-height: 1;
  }
  .gin-name .line-one {
    display: block;
    padding-left: 130px;
    font-size: 118px;
  }
  .gin-name .line-two {
    display: block;
    padding-left: 250px;
    margin-top: -28px;
    font-size: 118px;
  }
  .spirit {
    position: absolute;
    top: 405px;
    width: 100%;
    text-align: center;
    font-family: "Cormorant Garamond", serif;
    font-weight: 500;
    font-size: 22px;
    letter-spacing: 14px;
    padding-left: 14px;
    color: var(--ink);
  }
  .volume {
    position: absolute;
    top: 488px;
    width: 100%;
    text-align: center;
    font-family: "Cormorant Garamond", serif;
    font-weight: 600;
    font-size: 14px;
    letter-spacing: 0.5px;
    color: var(--fine);
  }
</style>
</head>
<body>
  <main class="canvas">
    <section class="label">
      <div class="sand-wash" role="img" aria-label="Soft sandy watercolour wash"></div>
      <div class="sea-wash" role="img" aria-label="Blue watercolour sea wash"></div>
      <p class="brand">Fernwhistle</p>
      <h1 class="gin-name">
        <span class="line-one">Harbor</span>
        <span class="line-two">Glow</span>
      </h1>
      <p class="spirit">GIN</p>
      <p class="volume">500ml | 37.5% ABV</p>
    </section>
  </main>
</body>
</html>
```